Advanced training flyer for defence industry - professional

U.S. Export Controls are some of the most complex and stringent in the world. The U.S. Government regulates the transfer of U.S. origin goods and technical data throughout the world, with the intent of preventing unauthorised transfer of technology and know-how.

These controls extend world-wide and can impact anyone dealing in U.S. controlled goods or technology.

This three-day advanced course is designed to give attendees a greater understanding of U.S. Export Controls from a non-U.S. perspective in practical and relevant terms. Though we will cover a lot of material the course is designed for practitioner with an existing knowledge.

We need a flyer design for an advanced course for the previously mentioned content.
Updates

Please include text boxes in order for the form to be completed online.

Target Market(s)

defence industry

Industry/Entity Type

Training

Requirements
Must have
• Please include text boxes so that the form can be completed online.
Nice to have
• flags incorporated

```html
<!DOCTYPE html>
<html lang="en">
<head>
<meta charset="utf-8">
<title>Advanced Export Controls Training Flyer</title>
<link href="https://fonts.googleapis.com/css2?family=PT+Sans:wght@400;700&family=PT+Sans+Narrow:wght@400;700&display=swap" rel="stylesheet">
<style>
:root{
  --green:#1a7a3c;
  --green-dark:#0f6332;
  --green-light:#2c9a4a;
  --ink:#1d1d1d;
  --grey-col:#eeeff0;
  --page:#ffffff;
  --stage:#2a2a2a;
  --sky:#a9c6e6;
  --navy:#2a3f8c;
}
*{box-sizing:border-box;margin:0;padding:0}
html,body{width:1200px;height:998px;overflow:hidden;background:var(--stage)}
.flyer{position:absolute;left:20px;top:90px;width:1160px;height:818px;background:var(--page);overflow:hidden;font-family:"PT Sans",sans-serif;color:var(--ink)}
.hero{position:absolute;left:0;top:0;width:100%;height:190px;
  background:linear-gradient(180deg,rgba(255,255,255,0) 55%,#fff 100%),
  linear-gradient(90deg,#c9cfe0 0%,#e7d9dc 10%,#b9d2ee 22%,var(--sky) 45%,#c4d9ee 70%,#9fb59a 88%,#8aa17f 100%)}
.fade-bottom{position:absolute;left:0;bottom:0;width:100%;height:26px;background:linear-gradient(180deg,#fff,#9db4e8)}
.col{position:absolute}
.intro{left:24px;top:160px;width:250px}
.brand{display:flex;align-items:center;gap:10px;height:88px;border-bottom:1px solid #999;margin-bottom:16px}
.brand-mark{width:42px;height:42px;border-radius:50%;background:var(--green);flex:none}
.brand-name{font-size:22px;line-height:24px;color:var(--green);font-weight:400}
.intro p{font-size:15.5px;line-height:19.8px;margin-bottom:14px}
.hl{color:var(--green)}
.price{position:absolute;left:24px;top:750px;font-family:"PT Sans Narrow",sans-serif;font-weight:700;font-size:20px;color:var(--green-dark)}
.who{left:312px;top:175px;width:244px}
.lead{font-size:18.5px;line-height:25px;padding-bottom:18px;border-bottom:1px solid #999;margin-bottom:14px}
.who h2{font-size:18px;color:var(--green-dark);font-weight:700}
.who p{font-size:15.5px;line-height:20px}
.quotes{position:absolute;left:305px;top:451px;width:244px;height:333px;background:var(--green-dark);padding:8px}
.quotes ul{list-style:none;border:1px solid #cfe3d5;height:100%;padding:12px 14px 0;position:relative}
.quotes li{color:#fff;font-size:13.4px;line-height:18px;text-align:center;padding:5px 0;border-bottom:1px solid #6fa882}
.quotes li:last-child{border:none}
.qmark{position:absolute;color:#fff;font-size:46px;font-weight:700;line-height:1;font-family:Georgia,serif}
.qmark.open{left:4px;top:2px}.qmark.close{right:4px;bottom:-14px}
.day{top:182px;width:176px;height:606px;background:var(--grey-col);padding:0 6px;overflow:hidden}
.day1{left:596px}.day2{left:781px}.day3{left:966px}
.tab{display:flex;align-items:center;height:16px;margin-bottom:10px;border-bottom:2px solid var(--green)}
.tab span{background:var(--green-dark);color:#fff;font-weight:700;font-size:11px;padding:2px 18px 1px 8px;clip-path:polygon(0 0,82% 0,100% 100%,0 100%)}
.day h3{font-size:11.5px;font-weight:400;color:var(--green);margin:9px 0 2px;line-height:13px}
.day h3:first-of-type{margin-top:0}
.day h4{font-size:11.5px;font-weight:400;color:var(--ink);margin:9px 0 2px;line-height:13px}
.day ul{list-style:none;font-family:"PT Sans Narrow",sans-serif;font-size:9.6px;line-height:13.2px}
.day li::before{content:"• "}
.day li.sub{padding-left:50px}
.day li.sub::before{content:"- "}
</style>
</head>
<body>
<main class="flyer">
  <div class="hero" role="img" aria-label="US and Australian flags with a fighter jet, helicopter and tank against a pale blue sky"></div>

  <section class="col intro">
    <div class="brand"><span class="brand-mark"></span><span class="brand-name">Northbridge Trade Compliance</span></div>
    <p><span class="hl">U.S. Export Controls</span> are some of the most complex and stringent in the world. The U.S. Government regulates the transfer of U.S. origin goods and technical data throughout the world, with the intent of preventing unauthorised transfer of technology and know-how.</p>
    <p>These controls extend world-wide &amp; can impact anyone dealing in U.S. controlled goods or technology.</p>
    <p><span class="hl">This three-day advanced course</span> is designed to give attendees a greater understanding of U.S. Export Controls from a non-U.S. perspective in practical and relevant terms. Though we will cover a lot of material the course is designed for practitioner with an existing knowledge.</p>
  </section>
  <div class="price">$2295.00 AUD per person inc GST</div>

  <section class="col who">
    <p class="lead">Guest presenters will deliver different aspects of the training program.</p>
    <h2>Who should attend:</h2>
    <p>Practitioners that work for dompanies that deal with U.S. based technology or that purchase U.S origin products, components or technology. The Advanced course assumes a basic understand of U.S. trade controls.</p>
  </section>

  <aside class="quotes">
    <ul>
      <span class="qmark open">&ldquo;</span>
      <li>Extremely well organized &amp; presented, very informative</li>
      <li>The Presenter was top rate</li>
      <li>Excellent overview of a complex topic</li>
      <li>A ‘must-do’ course for anyone working with defence articles</li>
      <li>Excellent presentation of a potentially dry subject</li>
      <li>Excellent course even for previously trained &amp; experienced Practitioners</li>
      <li>Extremely worthwhile</li>
      <span class="qmark close">&rdquo;</span>
    </ul>
  </aside>

  <section class="col day day1">
    <div class="tab"><span>DAY 1</span></div>
    <h3>EAR Introduction</h3>
    <ul><li>Key concepts</li><li>Export Administration Regulations</li><li>Bureau of Industry &amp; Security</li></ul>
    <h3>How To Classify Your Item</h3>
    <ul><li>How to determine the Export Control<br>&nbsp;&nbsp;Classification Number</li></ul>
    <h3>Technology Controls</h3>
    <ul><li>What technology is subject to EAR;</li><li>License exceptions</li><li>Foreign items incorporating controlled<br>&nbsp;&nbsp;U.S.-origin technology</li><li>Encryption under the EAR</li></ul>
    <h3>Technical data Considerations</h3>
    <ul><li>Controls on physical and intangible data</li><li>Deemed export and re-exports</li><li>Third country national issues</li></ul>
    <h3>EAR Exceptions</h3>
    <ul><li>Terms, provisions, applicability &amp;<br>&nbsp;&nbsp;use of Licence Exceptions</li><li>Changes to Exceptions</li><li>Restrictions governing the use of Exceptions</li><li>Distinction between list based &amp;<br>&nbsp;&nbsp;transaction based Licence Exceptions</li></ul>
    <h3>Deemed Export</h3>
    <ul><li>How to determine when deemed export<br>&nbsp;&nbsp;licenses are necessary</li></ul>
    <h3>Export Control Reform</h3>
    <ul><li>ITAR to EAR</li><li>600 series</li><li>Specially designed</li><li>Handling licenses and approvals</li></ul>
  </section>

  <section class="col day day2">
    <div class="tab"><span>DAY 2</span></div>
    <h3>ITAR Introduction</h3>
    <ul><li>Key concepts</li><li>International Traffic in Arms Regulations</li></ul>
    <h4>Understanding ITAR classifications<br>How to classify an item in the ITAR</h4>
    <h3>Re-exports &amp; re-transfers</h3>
    <ul><li>Licence free activity</li><li>Returning items to the U.S.</li></ul>
    <h3>ITAR approvals</h3>
    <ul><li>Licences</li><li>Agreements</li><li class="sub">Types of agreements</li><li class="sub">Sub-licensing</li><li class="sub">Dual nationals</li><li class="sub">NDA's</li><li class="sub">Amendments</li></ul>
    <h3>Brokering</h3>
    <ul><li>Extra-territorial application</li><li>Registration</li><li>Reporting requirements</li></ul>
    <h4>Destruction and Disposal of ITAR items</h4>
    <h4>Defence services involving ITAR controlled articles and technical data</h4>
    <h4>Recordkeeping for the ITAR</h4>
    <h3>Foreign Military Sales</h3>
    <ul><li>Letter of Offer</li><li>Third Party Re-transfer Approvals</li><li>Export Control Reform and FMS</li></ul>
    <h3>Export Control Reform</h3>
    <ul><li>The ITAR definition of Specially Designed</li></ul>
  </section>

  <section class="col day day3">
    <div class="tab"><span>DAY 2</span></div>
    <h3>COMPLIANCE &amp; ENFORCEMENT<br>Trade Control Compliance Framework</h3>
    <ul><li>Document development</li><li>Infrastructure</li><li>Risk assessments</li><li>Internal self assessments</li></ul>
    <h3>Enforcement</h3>
    <ul><li>U.S. enforcement</li><li>Fines and penalties</li><li>Case studies</li><li>Preventing violations</li></ul>
    <h3>NON-US ISSUES<br>Dual Nationals</h3>
    <ul><li>Anti-discrimination</li><li>Privacy</li></ul>
    <h3>AUSTRALIAN REGULATIONS</h3>
    <ul><li>Australia's System of Export Controls</li><li>Defence and Strategic Goods List?</li><li>Dual-Use List</li><li>Customs Act 1901</li><li>Defence Trade Controls Act 2012</li><li>Catch-All Legislation</li><li>Sanctions Legislation</li><li>Compliance philosophy</li><li>Non-compliance and penalties</li><li>Risk of diversion</li><li>Cyber security</li><li>Red flags</li><li>Self-Assessment Tool</li><li>AU-US Trade Co-operation Treaty</li><li>Managing the transition to intangibles</li></ul>
  </section>

  <div class="fade-bottom"></div>
</main>
</body>
</html>
```